Stylish Business Cards Wanted

- DOUBLE SIDED Design Required -

High end, edgy cards for a corporate and personal stylist. Must include logo,
Name: Belinda Forsey
Title: Director and Stylist
telephone : +61 8 8217 4592
email: belinda@thegarbledger.example
website: thegarbledger.example
Tag: Corporate Workwear & Uniform Specialist | Personal Stylist
Would like nice icons for telephone, email, website

Target Market(s)

Businesses wanting stylish uniforms, people wanting stylish wardrobes

Industry/Entity Type

Corporate Workwear Stylist

Contact Information for Business Card

I would like black, white and gold foiling incorporated in the design - possibly a touch of the other colours on my branding guide attached Name: Belinda Forsey Title: Director and Stylist telephone : +61 8 8217 4592 email: belinda@thegarbledger.example website: thegarbledger.example Tag: Corporate Workwear & Uniform Specialist | Personal Stylist Would like nice icons for telephone, email, website

Font styles to use
Other font styles liked:
• Raleway

Colors

Designer to choose colors to be used in the design.

Requirements
Must have
• Gold foil accents

```html
<!DOCTYPE html>
<html lang="en">
<head>
<meta charset="utf-8">
<title>The Garb Ledger – Business Card</title>
<link href="https://fonts.googleapis.com/css2?family=Open+Sans:wght@400;600&display=swap" rel="stylesheet">
<style>
  :root {
    --ink: #231f20;
    --gold: #e9b949;
    --paper: #ffffff;
  }
  html, body {
    margin: 0;
    padding: 0;
    width: 1200px;
    height: 1200px;
    overflow: hidden;
    background: var(--paper);
    font-family: "Open Sans", Arial, sans-serif;
  }
  .card {
    position: absolute;
    left: 270px;
    width: 660px;
    height: 416px;
    box-sizing: border-box;
    border: 3px solid var(--ink);
    background: var(--paper);
  }
  .card--front { top: 150px; }
  .card--back { top: 682px; }

  .wordmark {
    position: absolute;
    left: 0;
    right: 0;
    text-align: center;
    color: var(--ink);
    font-weight: 600;
    white-space: nowrap;
  }
  .card--front .wordmark { top: 82px; font-size: 32px; }
  .card--back .wordmark { top: 180px; font-size: 40px; }

  .info-band {
    position: absolute;
    left: -3px;
    right: -3px;
    top: 206px;
    bottom: -3px;
    background: var(--ink);
  }
  .info-band__rule {
    position: absolute;
    left: 3px;
    right: 3px;
    top: 4px;
    height: 3px;
    background: var(--paper);
  }
  .tagline {
    position: absolute;
    left: 56px;
    top: 50px;
    margin: 0;
    color: var(--gold);
    font-size: 12px;
    line-height: 15.5px;
  }
  .identity {
    position: absolute;
    left: 434px;
    top: 46px;
    color: var(--gold);
  }
  .identity__name {
    margin: 0;
    font-size: 24px;
    line-height: 30px;
    font-weight: 400;
  }
  .identity__title {
    margin: 0;
    font-size: 14.5px;
    line-height: 18px;
  }
  .contacts {
    position: absolute;
    left: 56px;
    top: 110px;
    margin: 0;
    padding: 0;
    list-style: none;
    color: var(--gold);
    font-size: 12px;
  }
  .contacts li {
    display: flex;
    align-items: center;
    height: 20.8px;
  }
  .contacts svg {
    width: 16px;
    height: 16px;
    margin-right: 7px;
    flex: none;
  }
</style>
</head>
<body>

<section class="card card--front">
  <div class="wordmark">The Garb Ledger</div>

  <div class="info-band">
    <div class="info-band__rule"></div>

    <p class="tagline">Corporate Workwear &amp; Uniform Specialist | Personal Stylist<br>Would like nice icons for telephone, email, website</p>

    <div class="identity">
      <h1 class="identity__name">Belinda Forsey</h1>
      <p class="identity__title">Director and Stylist</p>
    </div>

    <ul class="contacts">
      <li>
        <svg viewBox="0 0 24 24" aria-hidden="true"><path fill="#e9b949" d="M6.6 10.8a15.1 15.1 0 0 0 6.6 6.6l2.2-2.2a1 1 0 0 1 1-.25 11.4 11.4 0 0 0 3.6.57 1 1 0 0 1 1 1V20a1 1 0 0 1-1 1A17 17 0 0 1 3 4a1 1 0 0 1 1-1h3.5a1 1 0 0 1 1 1c0 1.25.2 2.45.57 3.57a1 1 0 0 1-.25 1z"/></svg>
        +61 8 8217 4592
      </li>
      <li>
        <svg viewBox="0 0 24 24" aria-hidden="true"><rect x="2" y="5" width="20" height="14" fill="#e9b949"/><path d="M2 5l10 8 10-8M2 19l7.5-7M22 19l-7.5-7" fill="none" stroke="#231f20" stroke-width="1.4"/></svg>
        belinda@thegarbledger.example
      </li>
      <li>
        <svg viewBox="0 0 24 24" aria-hidden="true"><g fill="none" stroke="#e9b949" stroke-width="1.4"><circle cx="12" cy="12" r="10"/><ellipse cx="12" cy="12" rx="4.5" ry="10"/><path d="M2 12h20M3.5 7h17M3.5 17h17M12 2v20"/></g></svg>
        thegarbledger.example
      </li>
    </ul>
  </div>
</section>

<section class="card card--back">
  <div class="wordmark">The Garb Ledger</div>
</section>

</body>
</html>
```